New Organic Skin Care Line Needs to Design a Product Label

***THE WINNER OF THIS PROJECT WILL MOST LIKELY BECOME THE EXCLUSIVE DESIGNER FOR OUR OTHER PRODUCT LABELS***

We need a label design for a new organic skin care product line called "Maple Fern Gala." This specific product is a 100% pure organic coconut oil. It's used for skin hydration, protection, and makeup removal.

Info to include on front label:

1. Logo: Maple Fern Gala (attached)
2. Product Name: Pure Coconut Oil (emphasize "organic" somewhere)
3. Slogan: Hydrate your skin and hair.
4. Size: 8 FL OZ 236mL

Attached is:

1. The brand logo "Maple Fern Gala" with a white background.
2. An image of the bottle we will use.
3. An image of the bottle with lines to show the size and placement of the label.
4. The brand logo "Maple Fern Gala" with a black background. (photoshop file)

What we need:

A simple mock up of the front side of the label on the bottle. We first want to know what it will look like on the bottle given the size and dimensions.

- We would like one label with a white background (including the logo with a white background).
- We would like a second label with a black background (including the logo with a black background, just need to make the black font white instead of black).

We can get a great idea of what to expect from the front side of the label so we will complete the back side once we identify a winner.
Updates

Apologies, but we are now using a different bottle. The previous one is now discontinued. Please view the two most recent images uploaded. One is an image of the new bottle by itself. The other is an image of that bottle with instructions. Please use your most recent designs on the new bottle. Feel free to make any modifications you see fit to compliment the new bottle shape. Added Friday, March 18, 2016

Reason: We are still working with the label company to finalize the size. Once the size is confirmed we will have to tweak labels based on finalized measurements.

Target Market(s)

Women, 18-70

Industry/Entity Type

Skin Care Product

Font styles to use
Decorative
Script

Requirements
Must have
• -"shabby sheek" and "cute" theme
• -soft organic feel
• -the ingredients are organic, pure, and natural. That should be an essence of the label.

```html
<!DOCTYPE html>
<html lang="en">
<head>
<meta charset="utf-8">
<title>Maple Fern Gala – Coconut Oil Labels</title>
<link rel="stylesheet" href="https://fonts.googleapis.com/css2?family=Amatic+SC:wght@400;700&family=Montserrat:wght@700&family=Raleway:wght@400;500&display=swap">
<style>
  :root {
    --paper: #ffffff;
    --ink-black: #000000;
    --bottle-glass: #e6e7e8;
    --brown: #8b5a32;
    --tan: #c59a6a;
    --badge-light: #e8cba0;
    --badge-dark: #a89576;
    --outline: #b9b9b9;
  }
  * { box-sizing: border-box; margin: 0; padding: 0; }
  html, body { width: 1200px; height: 1200px; overflow: hidden; background: var(--paper); }
  .sheet { position: relative; width: 1200px; height: 1200px; }

  .bottle, .flat-label { position: absolute; }
  .bottle { width: 325px; height: 770px; left: 60px; top: 8px; }
  .bottle--black { left: 292px; top: 392px; }
  .bottle svg, .flat-label svg { position: absolute; inset: 0; width: 100%; height: 100%; }

  .flat-label { left: 662px; width: 454px; height: 249px; }
  .flat-label--1 { top: 48px; }
  .flat-label--2 { top: 323px; }
  .flat-label--3 { top: 608px; }
  .flat-label--4 { top: 882px; }

  .line {
    position: absolute; left: 0; width: 100%;
    text-align: center; white-space: nowrap; line-height: 1;
  }
  .brand-name {
    font-family: 'Raleway', sans-serif; font-weight: 500;
    font-size: 9px; letter-spacing: 2px; text-transform: uppercase;
  }
  .organic { font-family: 'Raleway', sans-serif; font-weight: 400; }
  .product-bold { font-family: 'Montserrat', sans-serif; font-weight: 700; font-size: 40px; letter-spacing: 0.5px; }
  .product-tall { font-family: 'Amatic SC', cursive; font-weight: 700; transform: scaleX(0.79); }
  .tagline-soft { font-family: 'Raleway', sans-serif; font-size: 13px; letter-spacing: 2px; }
  .tagline-caps { font-family: 'Amatic SC', cursive; font-weight: 400; font-size: 17px; letter-spacing: 2.5px; text-transform: uppercase; }
  .size-badge {
    position: absolute; left: 50%; transform: translateX(-50%);
    border-radius: 50%; display: flex; flex-direction: column;
    align-items: center; justify-content: center;
    font-family: 'Raleway', sans-serif; color: var(--paper); line-height: 1;
  }

  .theme-white .brand-name, .theme-white .organic, .theme-white .product-bold, .theme-white .product-tall { color: var(--brown); }
  .theme-white .tagline-soft, .theme-white .tagline-caps { color: var(--tan); }
  .theme-white .size-badge { background: var(--badge-light); }
  .theme-black .brand-name, .theme-black .organic, .theme-black .product-bold,
  .theme-black .product-tall, .theme-black .tagline-soft, .theme-black .tagline-caps { color: var(--paper); }
  .theme-black .size-badge { background: var(--badge-dark); }

  .dash::before, .dash::after { content: ""; display: inline-block; width: 12px; height: 1px; background: currentColor; vertical-align: middle; margin: 0 8px; }
</style>
</head>
<body>
<div class="sheet">
  <svg width="0" height="0" style="position:absolute">
    <defs>
      <linearGradient id="wreath-tone" x1="0" y1="0" x2="0" y2="1">
        <stop offset="0" stop-color="#9cc93a"/>
        <stop offset="0.5" stop-color="#f2b233"/>
        <stop offset="1" stop-color="#7fb82e"/>
      </linearGradient>
      <radialGradient id="label-sheen" cx="0.5" cy="0.4" r="0.7">
        <stop offset="0" stop-color="#ffffff"/>
        <stop offset="1" stop-color="#dcdcdc"/>
      </radialGradient>
      <radialGradient id="label-dark" cx="0.5" cy="0.4" r="0.7">
        <stop offset="0" stop-color="#2a2a2a"/>
        <stop offset="1" stop-color="#000000"/>
      </radialGradient>
      <clipPath id="bottle-shape">
        <path d="M115,0 L210,0 L212,80 L207,92 Q212,300 283,505 A160,160 0 1 1 42,505 Q113,300 118,92 L113,80 Z"/>
      </clipPath>
    </defs>
  </svg>

  <!-- White bottle -->
  <div class="bottle bottle--white theme-white">
    <svg viewBox="0 0 325 770" role="img" aria-label="Glass bottle with round base">
      <path fill="var(--bottle-glass)" d="M115,0 L210,0 L212,80 L207,92 Q212,300 283,505 A160,160 0 1 1 42,505 Q113,300 118,92 L113,80 Z"/>
      <rect x="0" y="462" width="325" height="280" fill="url(#label-sheen)" clip-path="url(#bottle-shape)"/>
      <g role="img" aria-label="Wreath of green leaves and oil drops" fill="none" stroke="url(#wreath-tone)" stroke-width="12" stroke-linecap="round" opacity="0.85">
        <path d="M62,505 Q10,610 75,715"/>
        <path d="M263,505 Q315,610 250,715"/>
      </g>
    </svg>
    <div class="line brand-name" style="top:520px">Maple Fern Gala</div>
    <div class="line organic dash" style="top:560px;font-size:15px">100% PURE ORGANIC</div>
    <div class="line product-tall" style="top:571px;font-size:76px">COCONUT OIL</div>
    <div class="line tagline-caps" style="top:656px">Hydrate your skin and hair</div>
    <div class="size-badge" style="top:680px;width:40px;height:40px;font-size:8px">8 FL OZ<br><span style="font-size:10px">236mL</span></div>
  </div>

  <!-- Black bottle -->
  <div class="bottle bottle--black theme-black">
    <svg viewBox="0 0 325 770" role="img" aria-label="Glass bottle with round base">
      <path fill="var(--bottle-glass)" d="M115,0 L210,0 L212,80 L207,92 Q212,300 283,505 A160,160 0 1 1 42,505 Q113,300 118,92 L113,80 Z"/>
      <rect x="0" y="464" width="325" height="282" fill="url(#label-dark)" clip-path="url(#bottle-shape)"/>
      <g role="img" aria-label="Wreath of green leaves and oil drops" fill="none" stroke="url(#wreath-tone)" stroke-width="12" stroke-linecap="round" opacity="0.9">
        <path d="M52,500 Q0,610 68,722"/>
        <path d="M273,500 Q325,610 257,722"/>
      </g>
    </svg>
    <div class="line brand-name" style="top:512px">Maple Fern Gala</div>
    <div class="line organic dash" style="top:557px;font-size:15px">100% PURE ORGANIC</div>
    <div class="line product-tall" style="top:570px;font-size:76px">COCONUT OIL</div>
    <div class="line tagline-caps" style="top:652px">Hydrate your skin and hair</div>
    <div class="size-badge" style="top:676px;width:44px;height:44px;font-size:8px">8 FL OZ<br><span style="font-size:10px">236mL</span></div>
  </div>

  <!-- Flat label 1: white, bold -->
  <div class="flat-label flat-label--1 theme-white">
    <svg viewBox="0 0 454 249" aria-hidden="true">
      <path d="M40,1 L414,1 Q478,124 414,248 L40,248 Q-24,124 40,1 Z" fill="var(--paper)" stroke="var(--outline)" stroke-width="1"/>
      <g role="img" aria-label="Wreath of green leaves and oil drops" fill="none" stroke="url(#wreath-tone)" stroke-width="14" stroke-linecap="round" opacity="0.85">
        <path d="M90,18 Q15,124 90,232"/>
        <path d="M364,18 Q439,124 364,232"/>
      </g>
    </svg>
    <div class="line brand-name" style="top:52px">Maple Fern Gala</div>
    <div class="line organic" style="top:82px;font-size:21px">100% PURE ORGANIC</div>
    <div class="line product-bold" style="top:104px">COCONUT OIL</div>
    <div class="line tagline-soft" style="top:147px">Hydrate your skin and hair</div>
    <div class="size-badge" style="top:194px;width:28px;height:28px;font-size:5px">8 FL OZ<br>236mL</div>
  </div>

  <!-- Flat label 2: white, tall -->
  <div class="flat-label flat-label--2 theme-white">
    <svg viewBox="0 0 454 249" aria-hidden="true">
      <path d="M40,1 L414,1 Q478,124 414,248 L40,248 Q-24,124 40,1 Z" fill="var(--paper)" stroke="var(--outline)" stroke-width="1"/>
      <g role="img" aria-label="Wreath of green leaves and oil drops" fill="none" stroke="url(#wreath-tone)" stroke-width="14" stroke-linecap="round" opacity="0.85">
        <path d="M90,18 Q15,124 90,232"/>
        <path d="M364,18 Q439,124 364,232"/>
      </g>
    </svg>
    <div class="line brand-name" style="top:54px">Maple Fern Gala</div>
    <div class="line organic dash" style="top:86px;font-size:15px">100% PURE ORGANIC</div>
    <div class="line product-tall" style="top:98px;font-size:84px">COCONUT OIL</div>
    <div class="line tagline-caps" style="top:184px">Hydrate your skin and hair</div>
    <div class="size-badge" style="top:215px;width:22px;height:22px;font-size:4px">8 FL OZ<br>236mL</div>
  </div>

  <!-- Flat label 3: black, bold -->
  <div class="flat-label flat-label--3 theme-black">
    <svg viewBox="0 0 454 249" aria-hidden="true">
      <path d="M40,0 L414,0 Q478,124 414,249 L40,249 Q-24,124 40,0 Z" fill="var(--ink-black)"/>
      <g role="img" aria-label="Wreath of green leaves and oil drops" fill="none" stroke="url(#wreath-tone)" stroke-width="14" stroke-linecap="round" opacity="0.9">
        <path d="M90,18 Q15,124 90,232"/>
        <path d="M364,18 Q439,124 364,232"/>
      </g>
    </svg>
    <div class="line brand-name" style="top:52px">Maple Fern Gala</div>
    <div class="line organic" style="top:82px;font-size:21px">100% PURE ORGANIC</div>
    <div class="line product-bold" style="top:104px">COCONUT OIL</div>
    <div class="line tagline-soft" style="top:147px">Hydrate your skin and hair</div>
    <div class="size-badge" style="top:195px;width:28px;height:28px;font-size:5px">8 FL OZ<br>236mL</div>
  </div>

  <!-- Flat label 4: black, tall -->
  <div class="flat-label flat-label--4 theme-black">
    <svg viewBox="0 0 454 249" aria-hidden="true">
      <path d="M40,0 L414,0 Q478,124 414,249 L40,249 Q-24,124 40,0 Z" fill="var(--ink-black)"/>
      <g role="img" aria-label="Wreath of green leaves and oil drops" fill="none" stroke="url(#wreath-tone)" stroke-width="14" stroke-linecap="round" opacity="0.9">
        <path d="M90,18 Q15,124 90,232"/>
        <path d="M364,18 Q439,124 364,232"/>
      </g>
    </svg>
    <div class="line brand-name" style="top:54px">Maple Fern Gala</div>
    <div class="line organic dash" style="top:86px;font-size:15px">100% PURE ORGANIC</div>
    <div class="line product-tall" style="top:98px;font-size:84px">COCONUT OIL</div>
    <div class="line tagline-caps" style="top:190px">Hydrate your skin and hair</div>
    <div class="size-badge" style="top:218px;width:22px;height:22px;font-size:4px">8 FL OZ<br>236mL</div>
  </div>
</div>
</body>
</html>
```